Introducing YOUR Chatterloom page (design)

In search of the best design for our new Chatterloom page promoting our business. Do you have what it takes to contend? Must use our logoWe have included some info on what type of business we are, and what we do. The only image that is important at this time, is the company logo, we would like for this to be on the CL page.

Target Market(s)

all real estate brokers and agents, home owners, buyers, and sellers of real estate. anyone needing home repair work.

Industry/Entity Type

Business

Font styles to use
Serif
Sans Serif

Requirements
Must have
• Use of our logo, information as to who we are and what we do.
Nice to have
• customer testimonies, work related photos, ability to link to all social media, as well as our very own website.
Should not have
• plagiarized or copyrighted work of any sorts.

```html
<!DOCTYPE html>
<html lang="en">
<head>
<meta charset="utf-8">
<title>Keystone Home Repairs — Chatterloom Page Cover</title>
<link rel="stylesheet" href="https://fonts.googleapis.com/css2?family=Montserrat:wght@700&family=Tinos&display=swap">
<style>
  :root {
    --ink: #231f20;
    --slate: #3a3a3c;
    --grey-band: #7f7f7f;
    --accent-red: #df3a3f;
    --text-red: #d6353f;
    --paper: #ffffff;
    --frame: #9a9a9a;
    --serif: "Tinos", "Times New Roman", serif;
    --sans: "Montserrat", Arial, sans-serif;
  }
  html, body {
    margin: 0;
    padding: 0;
    width: 1200px;
    height: 459px;
    overflow: hidden;
    background: var(--paper);
  }
  .cover {
    position: relative;
    width: 1200px;
    height: 459px;
    box-sizing: border-box;
    border: 2px solid var(--frame);
    background: var(--paper);
    font-family: var(--serif);
    color: var(--ink);
  }
  .brand {
    position: absolute;
    left: 30px;
    top: 120px;
    display: flex;
    align-items: center;
    gap: 16px;
  }
  .brand-square {
    width: 38px;
    height: 38px;
    background: var(--accent-red);
    flex: none;
  }
  .brand-name {
    margin: 0;
    font-family: var(--sans);
    font-weight: 700;
    font-size: 33px;
    line-height: 1.15;
    color: var(--slate);
  }
  .service-area {
    position: absolute;
    left: 568px;
    top: 96px;
    font-size: 25px;
    line-height: 35px;
  }
  .service-area .tick {
    position: absolute;
    left: 4px;
    top: 4px;
  }
  .service-area p {
    margin: 0;
  }
  .service-area .first-line {
    padding-left: 72px;
  }
  .services {
    position: absolute;
    left: 839px;
    top: 36px;
    width: 326px;
    margin: 0;
    padding: 0;
    list-style: none;
  }
  .service {
    height: 50px;
    margin-bottom: 13px;
    color: var(--paper);
    font-size: 30px;
    line-height: 50px;
    text-align: center;
  }
  .service--grey { background: var(--grey-band); }
  .service--black { background: var(--ink); }
  .service--red { background: var(--accent-red); }
  .pitch {
    position: absolute;
    left: 20px;
    top: 296px;
    margin: 0;
    font-size: 29px;
    line-height: 45px;
  }
  .pitch .highlight {
    color: var(--text-red);
  }
  .contact {
    position: absolute;
    left: 836px;
    top: 304px;
  }
  .contact-label {
    margin: 0;
    font-size: 50px;
    line-height: 56px;
  }
  .contact-phone {
    margin: 0;
    font-size: 58px;
    line-height: 66px;
  }
</style>
</head>
<body>
  <main class="cover">
    <div class="brand">
      <span class="brand-square" aria-hidden="true"></span>
      <h1 class="brand-name">Keystone Home Repairs<br>And Maintenance</h1>
    </div>

    <div class="service-area">
      <svg class="tick" width="52" height="26" viewBox="0 0 52 26" aria-hidden="true">
        <path d="M0 4 L18 24 L52 0 L18 15 Z" fill="var(--accent-red)"/>
      </svg>
      <p class="first-line">Serving the</p>
      <p>Millbrook and</p>
      <p>surrounding areas</p>
    </div>

    <ul class="services">
      <li class="service service--grey">Carpentry</li>
      <li class="service service--black">Plumbing</li>
      <li class="service service--red">Doors &amp; Windows</li>
      <li class="service service--grey">Crawl Space &amp; Attics</li>
    </ul>

    <p class="pitch">
      Need help to get your <span class="highlight">Listing Ready to Show?</span><br>
      A complete <span class="highlight">Home Repair Solution?</span><br>
      Did an inspection reveal <span class="highlight">Repairs Needed Before Closing?</span>
    </p>

    <div class="contact">
      <p class="contact-label">Call us.</p>
      <p class="contact-phone">555-014-2270</p>
    </div>
  </main>
</body>
</html>
```